Visitenkarten-Design für Handel mit Handstrickgarnen
Zielgruppe
Handel mit Handstrickgarnen, besonders Farbverläufe und handgefärbte Garne, aber auch Design von Strickmode. Die Zielgruppe sind alle, die gerne stricken oder häkeln, insbesondere Frauen aller Altersgruppen.
Aufgabenstellung
Schöne Farbverläufe bzw. Farbharmonien sind mir besonders wichtig und sollten insgesamt ins Auge stechen ohne jedoch zu grell bunt zu wirken. Sanft ineinander fließende Farben wären ideal, gerne auch etwas kräftigere Farben. Das Motiv des Logos könnte auch im Negativ sein auf dunklerem Hintergrund.

```html
<!DOCTYPE html>
<html lang="de">
<head>
<meta charset="utf-8">
<title>Filomira – Visitenkarte</title>
<link href="https://fonts.googleapis.com/css2?family=Open+Sans:wght@300;400;600&display=swap" rel="stylesheet">
<style>
  :root {
    --stage: #ece9e4;
    --card-white: #ffffff;
    --taupe: #c2b9ad;
    --text-light: #ffffff;
    --brand: #8a2f7e;
    --hairline: #ecebea;
    --yarn-1: #e84a7a;
    --yarn-2: #f08a3c;
    --yarn-3: #f2c94c;
    --yarn-4: #6cc070;
    --yarn-5: #3aa6c9;
    --yarn-6: #5b5bc4;
    --yarn-7: #a24bb8;
  }
  * { margin: 0; padding: 0; box-sizing: border-box; }
  html, body { width: 1200px; height: 857px; overflow: hidden; }
  body {
    background: var(--stage);
    font-family: "Open Sans", Arial, sans-serif;
    display: flex;
    align-items: center;
    justify-content: center;
    gap: 44px;
  }
  .card {
    position: relative;
    width: 520px;
    height: 336px;
    box-shadow: 0 10px 28px rgba(60, 45, 30, 0.18);
    overflow: hidden;
  }
  .card--front { background: var(--card-white); }
  .card--back {
    background: var(--taupe);
    display: flex;
    align-items: center;
    justify-content: center;
  }
  .front-shape { position: absolute; inset: 0; width: 100%; height: 100%; }
  .brand {
    position: absolute;
    top: 32px;
    right: 32px;
    display: flex;
    align-items: center;
    gap: 10px;
  }
  .brand__dot {
    width: 38px; height: 38px;
    border-radius: 50%;
    flex: none;
  }
  .brand__dot--yarn {
    background: conic-gradient(from 200deg,
      var(--yarn-1), var(--yarn-2), var(--yarn-3), var(--yarn-4),
      var(--yarn-5), var(--yarn-6), var(--yarn-7), var(--yarn-1));
    box-shadow: inset 0 0 0 1px rgba(255,255,255,0.35);
  }
  .brand__name {
    font-weight: 600;
    font-size: 26px;
    letter-spacing: 2px;
    color: var(--brand);
    white-space: nowrap;
  }
  .back-brand { display: flex; align-items: center; gap: 16px; }
  .back-brand .brand__dot {
    width: 44px; height: 44px;
    border: 3px solid var(--text-light);
  }
  .back-brand .brand__name {
    font-size: 44px;
    color: var(--text-light);
    letter-spacing: 4px;
  }
  .contact {
    position: absolute;
    left: 34px;
    bottom: 34px;
    color: var(--text-light);
    text-transform: uppercase;
    font-weight: 300;
  }
  .contact__name { font-size: 27px; letter-spacing: 1px; line-height: 1.05; }
  .contact__role { font-size: 12px; letter-spacing: 0.5px; margin-bottom: 20px; }
  .contact__phones, .contact__web { font-size: 15px; line-height: 1.2; }
  .contact__phones { margin-bottom: 16px; }
</style>
</head>
<body>
  <section class="card card--front" aria-label="Visitenkarte Vorderseite">
    <svg class="front-shape" viewBox="0 0 520 336" preserveAspectRatio="none" aria-hidden="true">
      <line x1="300" y1="0" x2="520" y2="150" stroke="var(--hairline)" stroke-width="1"/>
      <line x1="520" y1="20" x2="450" y2="336" stroke="var(--hairline)" stroke-width="1"/>
      <path d="M0 62 C 170 20, 330 130, 382 336 L 0 336 Z" fill="var(--taupe)"/>
    </svg>
    <div class="brand">
      <span class="brand__dot brand__dot--yarn"></span>
      <span class="brand__name">FILOMIRA</span>
    </div>
    <div class="contact">
      <p class="contact__name">Vorname Name</p>
      <p class="contact__role">Position | Berufsbezeichnung</p>
      <p class="contact__phones">+49 157 777 777 77<br>+49 30 111 111 11</p>
      <p class="contact__web">name@firmenname.de<br>www.firmenname.de</p>
    </div>
  </section>

  <section class="card card--back" aria-label="Visitenkarte Rückseite">
    <div class="back-brand">
      <span class="brand__dot"></span>
      <span class="brand__name">FILOMIRA</span>
    </div>
  </section>
</body>
</html>
```